" Nossa empresa já possui um público ativo, que necessita de nossos serviços, ou seja, não precisamos trabalhar com a capacitação de clientes. Atendemos na grande maioria advogados, oficiais de justiça, servidores públicos, e por isso queremos uma marca de confiança, sólida e com personalidade. "

```html
<!DOCTYPE html>
<html lang="pt-BR">
<head>
<meta charset="utf-8">
<title>Capa de caderno — Ofício Predial Vale Norte</title>
<link rel="stylesheet" href="https://fonts.googleapis.com/css2?family=Montserrat:wght@500&display=swap">
<style>
  :root {
    --backdrop: #ececec;
    --cover: #ffffff;
    --copper: #a55f42;
    --ink: #2a2a2a;
  }
  html, body {
    margin: 0;
    padding: 0;
    width: 1200px;
    height: 1200px;
    overflow: hidden;
    background: var(--backdrop);
  }
  .canvas {
    position: relative;
    width: 1200px;
    height: 1200px;
  }
  .notebook-cover {
    position: absolute;
    left: 320px;
    top: 80px;
    width: 560px;
    height: 1040px;
    background: var(--cover);
    border-radius: 0 22px 22px 0;
    overflow: hidden;
    box-shadow: 0 2px 10px rgba(0,0,0,0.08);
  }
  .cover-waves {
    position: absolute;
    left: 0;
    bottom: 0;
    width: 560px;
    height: 260px;
    display: block;
  }
  .wave-copper { fill: var(--copper); }
  .wave-ink { fill: var(--ink); }
  .brand {
    position: absolute;
    left: 100px;
    top: 470px;
    display: flex;
    align-items: center;
    gap: 18px;
    color: var(--copper);
    font-family: "Montserrat", sans-serif;
    font-weight: 500;
    font-size: 34px;
    line-height: 1.2;
    letter-spacing: 0.02em;
  }
  .brand-dot {
    flex: none;
    width: 18px;
    height: 18px;
    border-radius: 50%;
    background: var(--copper);
  }
  .brand-name {
    margin: 0;
    font: inherit;
  }
</style>
</head>
<body>
  <main class="canvas">
    <section class="notebook-cover" aria-label="Capa do caderno">
      <div class="brand">
        <span class="brand-dot"></span>
        <p class="brand-name">Ofício Predial<br>Vale Norte</p>
      </div>

      <svg class="cover-waves" viewBox="0 0 560 260" aria-hidden="true">
        <path class="wave-copper"
              d="M0 84 C 120 40, 300 10, 560 4 L560 260 L0 260 Z"/>
        <path class="wave-ink"
              d="M0 128 C 150 92, 330 72, 560 78 L560 260 L0 260 Z"/>
      </svg>
    </section>
  </main>
</body>
</html>
```